Essential oil label for bottles

Looking to modify our current logo and label design. It looks too simple. I will attach images of our competitors to use as examples. Our company name is Lunvessa. We have 2 different bottles. Clear and amber color. Going forward, we will be using only the amber bottle. The other 2 images are the biggest sellers brands. We want to make some adjustments to ours.

Target Market(s)

Tradeport sales

Industry/Entity Type

Essential oil, perfume

Colors

Designer to choose only greyscale colors for use in the design.

Requirements
Nice to have
• A slight change to fonts and logo design. Maybe change the font and design of the word "Lunvessa" in our logo. Maybe add something to the label to make it stand out more but still keeping it clean and modern
Should not have
• No colors, besides, black, grays, whites, and off white.

```html
<!DOCTYPE html>
<html lang="en">
<head>
<meta charset="UTF-8">
<title>Lunvessa Fragrance Oil Labels</title>
<link rel="stylesheet" href="https://fonts.googleapis.com/css2?family=Montserrat:wght@500;600;700&display=swap">
<style>
  :root {
    --canvas: #f4f4f4;
    --label-light: #e8e8e8;
    --label-dark: #2f2f2f;
    --ink-dark: #4a4a4a;
    --ink-light: #ececec;
  }
  * { margin: 0; padding: 0; box-sizing: border-box; }
  html, body {
    width: 1200px;
    height: 960px;
    overflow: hidden;
    background: var(--canvas);
    font-family: "Montserrat", sans-serif;
  }
  .label-set {
    position: relative;
    width: 1200px;
    height: 960px;
  }
  .label {
    position: absolute;
    width: 420px;
    height: 600px;
    display: flex;
    flex-direction: column;
    align-items: center;
  }
  .label--light {
    left: 150px;
    top: 120px;
    background: var(--label-light);
    color: var(--ink-dark);
  }
  .label--dark {
    left: 630px;
    top: 240px;
    background: var(--label-dark);
    color: var(--ink-light);
  }
  .brand {
    margin-top: 112px;
    display: flex;
    align-items: center;
    gap: 16px;
  }
  .brand-mark {
    width: 12px;
    height: 12px;
    border-radius: 50%;
    background: currentColor;
  }
  .brand-name {
    font-size: 22px;
    font-weight: 600;
    letter-spacing: 0.55em;
    text-transform: uppercase;
  }
  .product-name {
    margin-top: 136px;
    width: 304px;
    border: 2px solid currentColor;
    text-align: center;
    font-size: 30px;
    font-weight: 700;
    letter-spacing: 0.12em;
    line-height: 36px;
    text-transform: uppercase;
    white-space: nowrap;
  }
  .product-type {
    margin-top: 22px;
    font-size: 16px;
    font-weight: 700;
    letter-spacing: 0.4em;
    text-transform: uppercase;
  }
  .notes {
    margin-top: 104px;
    display: flex;
    align-items: center;
    gap: 12px;
    font-size: 14px;
    font-weight: 600;
    text-transform: uppercase;
    white-space: nowrap;
  }
  .notes-divider {
    width: 2px;
    height: 18px;
    background: currentColor;
  }
  .volume {
    margin-top: 62px;
    font-size: 14px;
    font-weight: 700;
  }
</style>
</head>
<body>
<main class="label-set">
  <section class="label label--light">
    <div class="brand">
      <span class="brand-mark"></span>
      <span class="brand-name">Lunvessa</span>
    </div>
    <h1 class="product-name">White Tea</h1>
    <p class="product-type">Fragrance Oil</p>
    <p class="notes">
      <span>White Tea</span><span class="notes-divider"></span>
      <span>Orange</span><span class="notes-divider"></span>
      <span>Palo Santo</span>
    </p>
    <p class="volume">200ML</p>
  </section>

  <section class="label label--dark">
    <div class="brand">
      <span class="brand-mark"></span>
      <span class="brand-name">Lunvessa</span>
    </div>
    <h1 class="product-name">Dusk Grove</h1>
    <p class="product-type">Fragrance Oil</p>
    <p class="notes">
      <span>Oud Wood</span><span class="notes-divider"></span>
      <span>Leather</span><span class="notes-divider"></span>
      <span>Sandalwood</span>
    </p>
    <p class="volume">200ML</p>
  </section>
</main>
</body>
</html>
```